Colorful Live Music Concert Poster for Tin Harbor

Looking for a portrait oriented "poster" promoting the band's upcoming show at Marlow Lounge on Sunday, 3/22 at 8 pm, and social version (square format for Instagram). <br/><br/>Copy:<br/>Tin Harbor<br/>with The Pale Wires<br/><br/>Marlow Lounge <br/>Sunday, March 22<br/>8 pm<br/><br/>Poster must be consistent with band's overall branding seen on www.tinharborband.example and it's Tunevault page at https://music.example.com/artist/7QxRtaWpLeNmVcz2Ks9DuB?si=381fkTsYpWmaGHeLoRqdXC <br/><br/>BUT, we wouldn't mind taking in a slightly updated direction. A good example is the cover for our recent single Glad Today, which is consistent in theme and color palette while updating the design and color at the same time. <br/><br/>The attached files include some band logo art as well as examples of posters done for prior shows. <br/><br/>The posters need not include photos of the band, but if you are so inclined, we've uploaded some selects as well.<br/><br/>Thank you. <br/><br/>Wendell<br/>Tin Harbor

```html
<!DOCTYPE html>
<html lang="en">
<head>
<meta charset="utf-8">
<title>Tin Harbor – Poster Designs</title>
<link href="https://fonts.googleapis.com/css2?family=Josefin+Sans:wght@300;400&family=Montserrat:ital,wght@0,800;1,400&display=swap" rel="stylesheet">
<style>
  :root {
    --navy: #1f2d5c;
    --pink-top: #f497b1;
    --pink-mid: #ee7f9b;
    --pink-deep: #df6a89;
    --brick-light: #f7d5df;
    --brick-shade: #f0bccb;
    --arc-line: #c9e6e3;
    --photo-sky: #dfe5e8;
    --photo-warm: #b89684;
    --photo-dark: #3a3541;
    --sheet: #ffffff;
  }
  * { margin: 0; padding: 0; box-sizing: border-box; }
  html, body { width: 911px; height: 1200px; overflow: hidden; background: var(--sheet); }
  .sheet { position: relative; width: 911px; height: 1200px; }

  .sheet-title { position: absolute; left: 44px; top: 26px; display: flex; align-items: baseline; gap: 14px; color: var(--navy); }
  .sheet-title__main { font-family: "Montserrat", sans-serif; font-weight: 800; font-size: 54px; letter-spacing: 1px; }
  .sheet-title__sub { font-family: "Montserrat", sans-serif; font-style: italic; font-weight: 400; font-size: 23px; }

  .poster { position: absolute; overflow: hidden; color: var(--navy); }
  .poster--portrait { height: 610px; }
  .poster--square { height: 394px; }
  .poster--left { left: 42px; width: 395px; }
  .poster--right { left: 472px; width: 396px; }
  .poster--row1 { top: 110px; }
  .poster--row2 { top: 755px; }
  .poster__art { position: absolute; inset: 0; width: 100%; height: 100%; }

  .lineup { position: absolute; top: 34px; font-family: "Josefin Sans", sans-serif; font-weight: 400; text-transform: uppercase; }
  .lineup__headliner { font-size: 34px; line-height: 33px; letter-spacing: 3px; }
  .lineup__with { font-size: 18px; text-transform: none; margin: 8px 0 6px 36px; }
  .lineup__support { font-size: 32px; line-height: 34px; letter-spacing: 1px; }

  .details { position: absolute; font-family: "Josefin Sans", sans-serif; font-weight: 300; font-size: 17px; line-height: 25px; }
  .details__date { display: flex; align-items: center; gap: 6px; }
  .details__day { display: inline-flex; width: 31px; height: 31px; border-radius: 50%; background: var(--navy); color: var(--pink-top); align-items: center; justify-content: center; font-size: 17px; padding-top: 2px; }
  .poster--square .details { font-size: 15px; line-height: 23px; }
  .poster--square .details__day { width: 27px; height: 27px; font-size: 15px; }
</style>
</head>
<body>
<div class="sheet">
  <header class="sheet-title">
    <span class="sheet-title__main">PREVIEW</span>
    <span class="sheet-title__sub">2 Poster Designs</span>
  </header>

  <!-- Portrait, bricks direction -->
  <section class="poster poster--portrait poster--left poster--row1">
    <svg class="poster__art" viewBox="0 0 395 610" preserveAspectRatio="none">
      <defs>
        <linearGradient id="bgBricksTall" x1="0" y1="0" x2="0" y2="1">
          <stop offset="0" stop-color="var(--pink-top)"/>
          <stop offset="0.5" stop-color="var(--pink-mid)"/>
          <stop offset="1" stop-color="var(--pink-deep)"/>
        </linearGradient>
        <linearGradient id="stepsTall" x1="1" y1="0" x2="0" y2="1">
          <stop offset="0" stop-color="var(--brick-light)"/>
          <stop offset="1" stop-color="var(--brick-shade)"/>
        </linearGradient>
      </defs>
      <rect width="395" height="610" fill="url(#bgBricksTall)" role="img" aria-label="Background of repeating pink peaks"/>
      <polygon points="395,190 395,610 0,610 0,595" fill="url(#stepsTall)" role="img" aria-label="Isometric staircase of pale pink and navy bricks"/>
    </svg>
    <div class="lineup" style="left:34px">
      <div class="lineup__headliner">Tin<br>Harbor</div>
      <div class="lineup__with">with</div>
      <div class="lineup__support">The Pale<br>Wires</div>
    </div>
    <div class="details" style="left:33px; top:248px">
      <div>Marlow Lounge</div>
      <div class="details__date">Sunday, March <span class="details__day">22</span></div>
      <div>8 pm</div>
    </div>
  </section>

  <!-- Portrait, photo direction -->
  <section class="poster poster--portrait poster--right poster--row1">
    <svg class="poster__art" viewBox="0 0 396 610" preserveAspectRatio="none">
      <defs>
        <linearGradient id="bgWallTall" x1="0" y1="0" x2="0" y2="1">
          <stop offset="0" stop-color="var(--pink-top)"/>
          <stop offset="1" stop-color="var(--pink-deep)"/>
        </linearGradient>
        <linearGradient id="photoTall" x1="0" y1="0" x2="0" y2="1">
          <stop offset="0" stop-color="var(--photo-sky)"/>
          <stop offset="0.45" stop-color="var(--photo-warm)"/>
          <stop offset="1" stop-color="var(--photo-dark)"/>
        </linearGradient>
      </defs>
      <rect width="396" height="610" fill="url(#bgWallTall)" role="img" aria-label="Pink background with a faint brick wall"/>
      <circle cx="292" cy="482" r="177" fill="url(#photoTall)" role="img" aria-label="Photo of the two band members standing outdoors at dusk"/>
      <path d="M155 357 A190 190 0 0 1 396 318" fill="none" stroke="var(--arc-line)" stroke-width="1.5"/>
    </svg>
    <div class="lineup" style="left:34px">
      <div class="lineup__headliner">Tin<br>Harbor</div>
      <div class="lineup__with">with</div>
      <div class="lineup__support">The Pale<br>Wires</div>
    </div>
    <div class="details" style="left:33px; top:248px">
      <div>Marlow Lounge</div>
      <div class="details__date">Sunday, March <span class="details__day">22</span></div>
      <div>8 pm</div>
    </div>
  </section>

  <!-- Square, bricks direction -->
  <section class="poster poster--square poster--left poster--row2">
    <svg class="poster__art" viewBox="0 0 395 394" preserveAspectRatio="none">
      <defs>
        <linearGradient id="bgBricksSq" x1="0" y1="0" x2="0" y2="1">
          <stop offset="0" stop-color="var(--pink-top)"/>
          <stop offset="1" stop-color="var(--pink-deep)"/>
        </linearGradient>
        <linearGradient id="stepsSq" x1="1" y1="0" x2="0" y2="1">
          <stop offset="0" stop-color="var(--brick-light)"/>
          <stop offset="1" stop-color="var(--brick-shade)"/>
        </linearGradient>
      </defs>
      <rect width="395" height="394" fill="url(#bgBricksSq)" role="img" aria-label="Background of repeating pink peaks"/>
      <polygon points="395,122 395,394 122,394" fill="url(#stepsSq)" role="img" aria-label="Isometric staircase of pale pink and navy bricks"/>
    </svg>
    <div class="lineup" style="left:34px">
      <div class="lineup__headliner">Tin<br>Harbor</div>
      <div class="lineup__with">with</div>
      <div class="lineup__support">The Pale<br>Wires</div>
    </div>
    <div class="details" style="left:33px; top:238px">
      <div>Marlow Lounge</div>
      <div class="details__date">Sunday, March <span class="details__day">22</span></div>
      <div>8 pm</div>
    </div>
  </section>

  <!-- Square, photo direction -->
  <section class="poster poster--square poster--right poster--row2">
    <svg class="poster__art" viewBox="0 0 396 394" preserveAspectRatio="none">
      <defs>
        <linearGradient id="bgWallSq" x1="0" y1="0" x2="0" y2="1">
          <stop offset="0" stop-color="var(--pink-top)"/>
          <stop offset="1" stop-color="var(--pink-deep)"/>
        </linearGradient>
        <linearGradient id="photoSq" x1="0" y1="0" x2="0" y2="1">
          <stop offset="0" stop-color="var(--photo-sky)"/>
          <stop offset="0.45" stop-color="var(--photo-warm)"/>
          <stop offset="1" stop-color="var(--photo-dark)"/>
        </linearGradient>
      </defs>
      <rect width="396" height="394" fill="url(#bgWallSq)" role="img" aria-label="Pink background with a faint brick wall"/>
      <circle cx="300" cy="300" r="140" fill="url(#photoSq)" role="img" aria-label="Photo of the two band members standing outdoors at dusk"/>
      <path d="M205 172 A152 152 0 0 1 396 180" fill="none" stroke="var(--arc-line)" stroke-width="1.5"/>
    </svg>
    <div class="lineup" style="left:27px">
      <div class="lineup__headliner">Tin<br>Harbor</div>
      <div class="lineup__with">with</div>
      <div class="lineup__support">The Pale<br>Wires</div>
    </div>
    <div class="details" style="left:26px; top:232px">
      <div>Marlow Lounge</div>
      <div class="details__date">Sunday, March <span class="details__day">22</span></div>
      <div>8 pm</div>
    </div>
  </section>
</div>
</body>
</html>
```